clean web design for a recruitment company

We need a web design for a company called 'TORAVI' recruitment. We are a new age recruitment companies that selects people by their true nature, values and what they can bring to the table as a tangible talent. We are all here possessing a certain talent, whatever that could be that the world needs. The final design should communicate professionalism and strongly embedded etiquette we believe in and a branding promise 'Seeing ones true nature'. Our companies values are integrity, giving away to the community, cherishing the sharing of our talent, time and helping one another.

Target Market(s)

Gulf Countries

Industry/Entity Type

It Company

Number of Pages Required

1 page

Font styles to use
Serif

Requirements
Must have
• Clear and readable font, user friendly structure and easy navigation menus.
Nice to have
• Extra sort of ideas on images we may use, tag lines etc. sample sites we love site:https://www.velmorandi.example/
• http://www.tessabrankow.example/
• http://www.pebbleloomcraft.example/idea-gallery/
Should not have
• all sort of colors, big combination of fonts, images with people in the office or people in suits likewise all the typical industry web sites

```html
<!DOCTYPE html>
<html lang="en">
<head>
<meta charset="utf-8">
<title>TORAVI Recruitment</title>
<link rel="stylesheet" href="https://fonts.googleapis.com/css2?family=Arimo:wght@400;700&family=Source+Sans+3:wght@400;600&display=swap">
<style>
:root{
  --green:#37ad63;
  --magenta:#c2146e;
  --ink:#1d1d1d;
  --body:#3c3c3c;
  --line:#dcdcdc;
  --team-bg:#f1f0f2;
  --footer:#1f1f1f;
  --white:#ffffff;
}
*{margin:0;padding:0;box-sizing:border-box}
html,body{width:1200px;height:2546px;overflow:hidden;background:var(--white)}
body{position:relative;font-family:"Source Sans 3",Arial,sans-serif;color:var(--body)}
.abs{position:absolute}
h1,h2,h3,.nav a,.brand,.btn-fill,.btn-line{font-family:Arimo,Arial,sans-serif;font-weight:400}

/* header */
.site-header{top:0;left:0;width:1200px;height:153px;border-bottom:1px solid var(--line)}
.brand{left:0;width:1200px;top:22px;text-align:center;color:var(--ink)}
.brand-mark{width:36px;height:36px;background:var(--ink);margin:0 auto 14px}
.brand-name{font-size:26px;font-weight:700;letter-spacing:2px;line-height:1}
.brand-sub{font-size:10px;letter-spacing:4px;margin-top:3px}

.nav{top:153px;left:0;width:1200px;height:56px;display:flex;align-items:center;padding-left:75px;border-bottom:1px solid var(--line)}
.nav a{font-size:13px;color:var(--ink);text-decoration:none;height:56px;line-height:56px;text-align:center}
.nav a.active{background:#e0e0e0}

/* hero */
.hero{top:209px;left:0;width:1200px;height:572px;
  background:
    radial-gradient(ellipse 70% 55% at 50% 42%,rgba(190,190,186,.55) 0%,rgba(120,120,118,.25) 55%,rgba(0,0,0,0) 100%),
    linear-gradient(180deg,#3b3b3b 0%,#8d8c89 22%,#a3a29e 45%,#7d7b77 68%,#4a4540 80%,#2c2824 100%)}
.dots{top:748px;left:580px;display:flex;gap:6px}
.dots span{width:9px;height:9px;border-radius:50%;background:var(--white)}
.dots span.on{background:var(--green)}

/* signup band */
.signup{top:781px;left:0;width:1200px;height:95px;background:var(--green);color:var(--white)}
.signup h2{position:absolute;left:76px;top:21px;font-size:24px;font-weight:700}
.signup p{position:absolute;left:76px;top:56px;font-size:13px}
.signup .field{position:absolute;top:30px;height:34px;background:var(--white);color:#555;font-size:13px;padding:9px 14px}
.signup .go{position:absolute;left:1070px;top:18px;width:60px;height:60px;border-radius:50%;background:var(--magenta);border:2px solid #e8a2c8;color:var(--white);font-size:13px;display:flex;align-items:center;justify-content:center;text-align:center;line-height:1}

/* welcome */
.welcome h1{top:930px;left:0;width:1200px;text-align:center;font-size:28px;color:var(--ink)}
.welcome h1 em{font-style:normal;color:var(--magenta)}
.welcome p{top:982px;left:78px;width:1042px;font-size:13px;line-height:21.5px;text-align:justify;text-align-last:center;color:var(--ink)}
.btn-fill{top:1091px;left:529px;width:141px;height:41px;background:var(--magenta);color:var(--white);font-size:13px;letter-spacing:1px;display:flex;align-items:center;justify-content:center}

/* jobs */
.jobs{top:1176px;left:0;width:1200px;height:572px;background:linear-gradient(160deg,#c75a5a 0%,#e8906a 25%,#b24f7e 55%,#3c2e6a 80%,#1e2452 100%)}
.section-title{left:0;width:1200px;text-align:center;font-size:30px;color:var(--ink)}
.job{width:502px;height:149px;background:var(--white)}
.job-logo{position:absolute;left:12px;top:12px;width:123px;height:125px;display:flex;align-items:center;justify-content:center;color:var(--white);font-family:Arimo,Arial,sans-serif;font-size:17px;font-weight:700}
.job-city{position:absolute;left:157px;top:14px;font-size:11px;color:#888}
.job h3{position:absolute;left:157px;top:32px;font-size:22px;color:var(--green)}
.job p{position:absolute;left:157px;top:67px;width:305px;font-size:12px;line-height:20px;color:var(--ink)}
.job .type{position:absolute;left:157px;top:113px;font-size:12px;color:var(--magenta)}
.btn-line{top:1655px;left:502px;width:199px;height:45px;border:2px solid var(--white);color:var(--white);font-size:14px;letter-spacing:1px;display:flex;align-items:center;justify-content:center}

/* team */
.team{top:1748px;left:0;width:1200px;height:470px;background:var(--team-bg)}
.member{top:1857px;width:191px;height:303px;background:var(--white);text-align:center}
.member-photo{height:153px;background:linear-gradient(160deg,#c9d6e2,#8ea6bd)}
.member h3{font-size:17px;color:var(--green);margin-top:16px}
.member p{font-size:12px;line-height:20px;color:var(--ink);margin:12px 20px 0}
.member .more{display:block;font-size:11px;color:var(--green);margin-top:12px;letter-spacing:.5px}

/* clients */
.client{top:2325px;width:131px;height:76px;border:1px solid #cfcfcf;display:flex;align-items:center;justify-content:center;text-align:center;font-family:Arimo,Arial,sans-serif;font-size:19px;line-height:1.2;color:var(--ink)}
.arrow{top:2350px;width:40px;height:40px}

/* footer */
.site-footer{top:2450px;left:0;width:1200px;height:96px;background:var(--footer)}
.site-footer small{position:absolute;left:76px;top:44px;font-size:12px;color:#ddd}
.social{position:absolute;left:966px;top:38px;display:flex;gap:10px}
.social span{width:27px;height:27px;border-radius:50%;background:var(--white)}
</style>
</head>
<body>

<header class="site-header abs">
  <div class="brand abs">
    <div class="brand-mark"></div>
    <div class="brand-name">TORAVI</div>
    <div class="brand-sub">RECRUITMENT</div>
  </div>
</header>

<nav class="nav abs">
  <a href="#" class="active" style="width:96px">HOME</a>
  <a href="#" style="width:136px">TEAM</a>
  <a href="#" style="width:137px">METHODOLOGY</a>
  <a href="#" style="width:198px">SPECIALIST AREAS</a>
  <a href="#" style="width:129px">CLIENTS</a>
  <a href="#" style="width:166px">CANDIDATES</a>
  <a href="#" style="width:138px">TORAVI GROUP</a>
</nav>

<section class="hero abs" role="img" aria-label="Black and white gallery wall of framed portrait photographs above a dark wooden floor"></section>
<div class="dots abs"><span class="on"></span><span></span><span></span><span></span></div>

<section class="signup abs">
  <h2>Seeing ones true nature</h2>
  <p>Nam libero tempore, cum soluta nobis est eligendi optio cumque nihil impedit quo min situd.</p>
  <div class="field" style="left:694px;width:173px">First Name</div>
  <div class="field" style="left:879px;width:175px">E-Mail</div>
  <div class="go">Get<br>it!</div>
</section>

<section class="welcome">
  <h1 class="abs">Welcome to Our Site <em>Mainpage</em></h1>
  <p class="abs">Lorem ipsum dolor sit amet, consectetur adipisic ing elit, sed do eiusmod tempor incididunt ut labore et dolore magna aliqua. Ut enim ad minim veniam, quis nostrud exercitaullamco. Lorem ipsum dolor sit amet, consectetur adipisic ing elit, sed do eiusmod tempor incididunt ut labore et dolore magna aliqua. Ut enim ad minim veniam, quis nostrud exercitaullamco.Lorem ipsum dolor sit amet, consectetur adipisic ing elit, sed do eiusmod tempor incididunt ut labore et dolore magna aliqua. Ut enim ad minim veniam, quis nostrud exercitaullamco incididunt ut labore et dolore magna aliqua.</p>
  <div class="btn-fill abs">LEARN MORE</div>
</section>

<section class="jobs abs" role="img" aria-label="Soft low-poly gradient backdrop in coral, pink and deep indigo"></section>
<h2 class="section-title abs" style="top:1228px">Featured Job’s</h2>

<article class="job abs" style="left:75px;top:1295px">
  <div class="job-logo" style="background:#1f6fd6">Skylark</div>
  <span class="job-city">London</span>
  <h3>Product Designer</h3>
  <p>Lorem ipsum dolor sit amet, consectetur adipisic ing elit, sed do eiusmod tempor incididunt ut labore</p>
  <span class="type">PART TIME / FULL TIME</span>
</article>
<article class="job abs" style="left:623px;top:1295px">
  <div class="job-logo" style="background:#e3f01a;color:#111">Hivora</div>
  <span class="job-city">London</span>
  <h3>Product Designer</h3>
  <p>Lorem ipsum dolor sit amet, consectetur adipisic ing elit, sed do eiusmod tempor incididunt ut labore</p>
  <span class="type">PART TIME / FULL TIME</span>
</article>
<article class="job abs" style="left:75px;top:1468px">
  <div class="job-logo" style="background:#dcdcda" role="img" aria-label="Company logo placeholder"></div>
  <span class="job-city">London</span>
  <h3>Product Designer</h3>
  <p>Lorem ipsum dolor sit amet, consectetur adipisic ing elit, sed do eiusmod tempor incididunt ut labore</p>
  <span class="type">PART TIME / FULL TIME</span>
</article>
<article class="job abs" style="left:623px;top:1468px">
  <div class="job-logo" style="background:#8e2a38">Snipwell</div>
  <span class="job-city">London</span>
  <h3>Product Designer</h3>
  <p>Lorem ipsum dolor sit amet, consectetur adipisic ing elit, sed do eiusmod tempor incididunt ut labore</p>
  <span class="type">PART TIME / FULL TIME</span>
</article>
<div class="btn-line abs">VIEW MORE JOBS</div>

<section class="team abs"></section>
<h2 class="section-title abs" style="top:1806px">Our Team</h2>

<div class="member abs" style="left:75px"><div class="member-photo" role="img" aria-label="Team member portrait photo"></div><h3>Lina Marsh</h3><p>Lorem ipsum dolor sit amet, consectetur adipisic ing elit, sed do eiusmod.</p><span class="more">READ MORE</span></div>
<div class="member abs" style="left:290px"><div class="member-photo" role="img" aria-label="Team member portrait photo"></div><h3>Omar Haddad</h3><p>Lorem ipsum dolor sit amet, consectetur adipisic ing elit, sed do eiusmod.</p><span class="more">READ MORE</span></div>
<div class="member abs" style="left:506px"><div class="member-photo" role="img" aria-label="Team member portrait photo"></div><h3>Karim</h3><p>Lorem ipsum dolor sit amet, consectetur adipisic ing elit, sed do eiusmod.</p><span class="more">READ MORE</span></div>
<div class="member abs" style="left:721px"><div class="member-photo" role="img" aria-label="Team member portrait photo"></div><h3>Nadia Farah</h3><p>Lorem ipsum dolor sit amet, consectetur adipisic ing elit, sed do eiusmod.</p><span class="more">READ MORE</span></div>
<div class="member abs" style="left:934px"><div class="member-photo" role="img" aria-label="Team member portrait photo"></div><h3>Idris Vale</h3><p>Lorem ipsum dolor sit amet, consectetur adipisic ing elit, sed do eiusmod.</p><span class="more">READ MORE</span></div>

<section class="clients">
  <h2 class="section-title abs" style="top:2266px">Our Clients</h2>
  <svg class="arrow abs" style="left:87px" viewBox="0 0 40 40"><circle cx="20" cy="20" r="19" fill="none" stroke="#cfcfcf" stroke-width="1.5"/><path d="M23 13l-7 7 7 7" fill="none" stroke="#555" stroke-width="2"/></svg>
  <div class="client abs" style="left:166px">Client<br>Logo</div>
  <div class="client abs" style="left:314px">Client<br>Logo</div>
  <div class="client abs" style="left:462px">Client<br>Logo</div>
  <div class="client abs" style="left:609px">Client<br>Logo</div>
  <div class="client abs" style="left:757px">Client<br>Logo</div>
  <div class="client abs" style="left:905px">Client<br>Logo</div>
  <svg class="arrow abs" style="left:1071px" viewBox="0 0 40 40"><circle cx="20" cy="20" r="19" fill="none" stroke="#cfcfcf" stroke-width="1.5"/><path d="M17 13l7 7-7 7" fill="none" stroke="#999" stroke-width="2"/></svg>
</section>

<footer class="site-footer abs">
  <small>Copyright ©2015, Yoursite. All Right Reserved.</small>
  <div class="social" aria-label="Social links"><span></span><span></span><span></span><span></span><span></span></div>
</footer>

</body>
</html>
```